Business card design needed

We are a boutique law firm within the Melbourne CBD.

You will need to upload our company logo which is to go on the left hand side of the business card - we then have a Legal Guild of Carrowmere logo to go perhaps on the bottom right hand side (color)

On the back we would like the website details

www.hartwellsolicitors.com.au - with a small logo
Updates

Thank you designers for all your great submissions.  Just going through the designs and we will choose one within the next couple of days.

Kind Regards
Hartwells Solicitors Pty Ltd

Industry/Entity Type

Boutique

Contact Information for Business Card

Dominic Hartwell
Principal
Level 6, 47 Penrose Street
Melbourne VIC Australia 3000
T+61 3 9555 0142 F+61 3 9555 0187
dominic@hartwellsolicitors.com.au
M 0491 570 156

```html
<!DOCTYPE html>
<html lang="en">
<head>
<meta charset="utf-8">
<title>Hartwells Solicitors – Business Card</title>
<link rel="stylesheet" href="https://fonts.googleapis.com/css2?family=Questrial&display=swap">
<style>
  :root {
    --bg: #d9d6d2;
    --card: #f4f4f4;
    --card-shade: #e3e3e3;
    --ink: #111111;
    --black: #050505;
    --white: #ffffff;
    --rule: #444444;
    --badge: #2f7fb8;
  }
  * { margin: 0; padding: 0; box-sizing: border-box; }
  html, body { width: 1200px; height: 900px; overflow: hidden; }
  body {
    background: var(--bg);
    font-family: "Questrial", "Century Gothic", sans-serif;
    color: var(--ink);
    position: relative;
  }
  .card {
    position: absolute;
    left: 300px;
    width: 600px;
    height: 343px;
    background: linear-gradient(180deg, var(--card) 0%, var(--card-shade) 100%);
    box-shadow: 0 6px 18px rgba(0,0,0,.25);
    overflow: hidden;
  }
  .card--back { top: 72px; }
  .card--front { top: 485px; }

  /* back */
  .back-band {
    position: absolute; left: 0; top: 0; width: 100%; height: 200px;
    background: var(--black);
  }
  .back-brand {
    position: absolute; left: 40px; top: 148px;
    display: flex; align-items: center; gap: 12px;
    color: var(--white); font-size: 30px;
  }
  .brand-square { width: 22px; height: 22px; background: var(--white); }
  .back-web {
    position: absolute; right: 36px; top: 162px;
    color: var(--white); font-size: 19px; letter-spacing: .3px;
  }
  .guild-badge {
    position: absolute; right: 40px; top: 228px;
    width: 52px; height: 52px; border-radius: 50%;
    background: var(--badge);
  }

  /* front */
  .front-logo {
    position: absolute; left: 245px; top: 38px;
    width: 300px; height: 74px; background: var(--black);
    display: flex; align-items: center; padding-left: 22px; gap: 12px;
    color: var(--white); font-size: 30px;
  }
  .front-logo .brand-square { width: 20px; height: 20px; }
  .holder-name {
    position: absolute; left: 70px; top: 190px; font-size: 22px;
  }
  .contact-list {
    position: absolute; left: 322px; top: 140px;
    border-left: 1.5px solid var(--rule);
    padding: 4px 0 4px 14px;
    list-style: none; font-size: 13px; line-height: 21px;
  }
  .contact-list li { display: flex; align-items: center; gap: 10px; white-space: nowrap; }
  .contact-list svg { width: 12px; height: 12px; flex: none; }
  .address-rule {
    position: absolute; left: 30px; right: 30px; top: 292px;
    border-top: 1px solid var(--rule);
  }
  .address-line {
    position: absolute; left: 30px; right: 30px; top: 300px;
    font-size: 12.5px; white-space: nowrap;
  }
</style>
</head>
<body>

<section class="card card--back" aria-label="Card back">
  <div class="back-band"></div>
  <div class="back-brand"><span class="brand-square"></span><span>Hartwells</span></div>
  <p class="back-web">www.hartwellsolicitors.com.au</p>
  <div class="guild-badge" role="img" aria-label="Legal Guild of Carrowmere accreditation badge"></div>
</section>

<section class="card card--front" aria-label="Card front">
  <div class="front-logo"><span class="brand-square"></span><span>Hartwells</span></div>
  <p class="holder-name">Dominic Hartwell</p>
  <ul class="contact-list">
    <li><svg viewBox="0 0 12 12"><rect x="3" y="0.5" width="6" height="11" rx="1" fill="none" stroke="#111" stroke-width="1.2"/><circle cx="6" cy="9.5" r=".8" fill="#111"/></svg>0491 570 156</li>
    <li><svg viewBox="0 0 12 12"><circle cx="6" cy="6" r="5.2" fill="none" stroke="#111" stroke-width="1"/><path d="M4 3.5c0 3 1.5 5 4.5 5.2l.3-1.3-1.3-.6-.6.7C5.8 7 5 6 4.8 5l.7-.6-.5-1.4z" fill="#111"/></svg>+61 3 9555 0142</li>
    <li><svg viewBox="0 0 12 12"><rect x="3" y="1" width="6" height="4" fill="none" stroke="#111"/><rect x="1" y="5" width="10" height="6" rx="1" fill="#111"/></svg>+61 3 9555 0187</li>
    <li><svg viewBox="0 0 12 12"><text x="0" y="10.5" font-size="12" font-family="sans-serif" fill="#111">@</text></svg>dominic@hartwellsolicitors.com.au</li>
  </ul>
  <div class="address-rule"></div>
  <p class="address-line">Principal Hartwells Solicitors Pty Ltd Level 6, 47 Penrose Street Melbourne VIC Australia 3000</p>
</section>

</body>
</html>
```